Graphics Design of Physics Book

Hi
Size : 8" x 11.25"
We are education book Publication Company and would like to have book cover for "Physics" it has 4 volumes. All 4 having the same color scheme and design except the volume no.
Blue is my personal favorite but u can use any color. Want to have a band at the bottom of the cover to place our Logo “VORLIN Education” a PDF of the same is attached, or you can place logo anywhere according to ur design.
I need “Physics” as title of the book to be visible prominently.
And volume and volume no. should also be Visible and eye catching I prefer a Graphic to enhance the Volume No.
A background pattern can also be a option (it should be vector form so that color can be change later)
Please do not offer any cut and paste design I need very professional presentation.
Volume and Number can be in metallic 3D (CMYK) effect.
only Professional presentation will get feedback.
I have provided a sample artwork for reference do not follow it but can be a reference what I needed !

Target Market(s)

Students Class 9th to 12th

Industry/Entity Type

Education

Font styles to use
Serif

Colors
3176b5
0555a3
85abd2
cadf82
abd036
9bcb3c

Requirements
Must have
• Eye catching.
• “Physics” as title of the book to be visible prominently.
• volume and volume no. should also be Visible and eye catching
• I prefer a Graphic to enhance the Volume No.
• Icons for
• 1. Questions and answers
• 2. Theory Notes
• 3. Tips & Tricks
• 4. Previous Year's Reference Questions
• 5. Covers Complete Syllabus
Nice to have
• decent seamless background or metallic 3d effect (not to be print in special Ink) design should only be in CMYK.
Should not have
• Physics related Pictures or Icons (Specially E=mc2) or any scientist photograph or I Need pure graphic design

```html
<!DOCTYPE html>
<html lang="en">
<head>
<meta charset="utf-8">
<title>Physics Volume 4 Cover</title>
<link href="https://fonts.googleapis.com/css2?family=Archivo+Black&family=Oswald:wght@400&family=Roboto+Slab:wght@400&display=swap" rel="stylesheet">
<style>
  :root {
    --deep-violet: #2a1a6c;
    --indigo: #253d92;
    --royal-blue: #0a78bb;
    --sky: #85abd2;
    --lavender: #b6b1d6;
    --ink: #0f1220;
    --band-light: #f4f4f6;
    --band-dark: #8d8f97;
    --bullet: #9a8fcf;
  }
  html, body {
    margin: 0;
    padding: 0;
    width: 854px;
    height: 1200px;
    overflow: hidden;
  }
  .cover {
    position: relative;
    width: 854px;
    height: 1200px;
    overflow: hidden;
    background: linear-gradient(180deg,
      var(--deep-violet) 0%,
      var(--deep-violet) 28%,
      var(--indigo) 46%,
      var(--royal-blue) 60%,
      #3f86c4 72%,
      var(--sky) 84%,
      #5a4fb0 100%);
  }
  .light-burst {
    position: absolute;
    inset: 0;
    background:
      radial-gradient(ellipse 420px 160px at 470px 950px, rgba(255,255,255,0.95) 0%, rgba(255,255,255,0.55) 30%, rgba(255,255,255,0) 75%),
      radial-gradient(ellipse 600px 260px at 450px 1000px, rgba(200,225,250,0.6) 0%, rgba(200,225,250,0) 70%);
  }
  .graphics {
    position: absolute;
    inset: 0;
  }
  .title {
    position: absolute;
    left: 50px;
    top: 50px;
    width: 754px;
    margin: 0;
    font-family: "Roboto Slab", serif;
    font-weight: 400;
    font-size: 178px;
    line-height: 1;
    letter-spacing: 2px;
    text-align: center;
    color: var(--lavender);
  }
  .publisher {
    position: absolute;
    left: 0;
    width: 854px;
    top: 1010px;
    text-align: center;
    font-family: "Archivo Black", sans-serif;
    font-size: 30px;
    color: var(--ink);
  }
  .feature-band {
    position: absolute;
    left: 0;
    top: 1092px;
    width: 854px;
    height: 48px;
    background: linear-gradient(180deg, var(--band-dark) 0%, var(--band-light) 22%, #ffffff 50%, #d4d5da 80%, var(--band-dark) 100%);
    display: flex;
    align-items: center;
    justify-content: center;
    gap: 9px;
    font-family: "Oswald", sans-serif;
    font-size: 14px;
    color: var(--ink);
    white-space: nowrap;
  }
  .feature {
    display: flex;
    align-items: center;
    gap: 6px;
  }
  .feature::before {
    content: "";
    width: 14px;
    height: 14px;
    border-radius: 50%;
    background: var(--bullet);
  }
</style>
</head>
<body>
<div class="cover">
  <div class="light-burst"></div>

  <svg class="graphics" width="854" height="1200" viewBox="0 0 854 1200">
    <defs>
      <linearGradient id="metal" x1="0" y1="0" x2="1" y2="0">
        <stop offset="0" stop-color="#f2f2f2"/>
        <stop offset="0.35" stop-color="#9a9ca0"/>
        <stop offset="0.55" stop-color="#ffffff"/>
        <stop offset="0.8" stop-color="#6e7075"/>
        <stop offset="1" stop-color="#d8d9db"/>
      </linearGradient>
      <path id="numeral-four" fill-rule="evenodd"
        d="M512 266 L700 266 L700 584 L764 584 L764 768 L700 768 L700 896 L440 896 L440 768 L252 768 L232 560 Z
           M512 416 L512 584 L352 584 Z"/>
    </defs>

    <line class="sweep-line" x1="364" y1="0" x2="432" y2="340" stroke="#0c0c18" stroke-width="2"/>
    <line class="sweep-line" x1="545" y1="900" x2="572" y2="1200" stroke="#0c0c18" stroke-width="2" opacity="0.6"/>

    <g class="volume-word">
      <g fill="var(--ink)">
        <text transform="translate(212 892) rotate(-90)" font-family="Archivo Black, sans-serif" font-size="138" textLength="620" lengthAdjust="spacingAndGlyphs">VOLUME</text>
        <text transform="translate(206 884) rotate(-90)" font-family="Archivo Black, sans-serif" font-size="138" textLength="620" lengthAdjust="spacingAndGlyphs">VOLUME</text>
      </g>
      <text transform="translate(198 876) rotate(-90)" fill="url(#metal)" font-family="Archivo Black, sans-serif" font-size="138" textLength="620" lengthAdjust="spacingAndGlyphs">VOLUME</text>
    </g>

    <g class="volume-number">
      <g fill="var(--ink)">
        <use href="#numeral-four" transform="translate(32 58)"/>
        <use href="#numeral-four" transform="translate(24 44)"/>
        <use href="#numeral-four" transform="translate(16 29)"/>
        <use href="#numeral-four" transform="translate(8 15)"/>
      </g>
      <use href="#numeral-four" fill="var(--lavender)"/>
    </g>
  </svg>

  <h1 class="title">PHYSICS</h1>

  <div class="publisher">VORLIN Education</div>

  <div class="feature-band">
    <span class="feature">Questions and answers</span>
    <span class="feature">Theory Notes</span>
    <span class="feature">Tips &amp; Tricks</span>
    <span class="feature">Previous Year's Reference Questions</span>
    <span class="feature">Covers Complete Syllabus</span>
  </div>
</div>
</body>
</html>
```